New business card for Building services company

I own a small 1 person business which primarily works at heights. I gain access to my work areas via ladders and use safety harnesses. I conduct gutter cleaning, roof cleaning with a pressure cleaner(water blaster), ground level pressure cleaning (driveways, footpaths and walls), I also do small handy-man jobs & gardening/ tree trimming.

I have just had a logo designed by Sketch Hive, which I will upload. I'd like to see the themes followed through.
I like the colour of aqua or the colours what is in the logo.

I live in tropical north Queensland in Cairns, Australia. It is where the rain forest meets the Coral Lantern Shoal. On average it is 30+ degrees C.
Updates

Hello all designers. Thankyou for all the submissions so far. The following are my business details which I need on the card-

VERNO Roof, Gutter & Pressure Cleaning Services.
Director -Dale Marwick
Ph 0417385026
Email- roofcleaning@plovernet.example.au
ABN -48 902 317 254

Please include the following services which my business conducts-
*Gutter Cleaning
*Pressure Cleaning- Roof's, Driveways etc
*Minor Roof, Gutter & Building Maintenance
*Garden waste removal & complex cleanups

Public Liability upto $10 Million
Working at Heights Cert.

Quote-                                     Date-

Hi everyone,  could you please ensure you have -"Quote" and "Date" on the card. I'll need space to hand write details on the card for the specific details.        

Requirements
Must have
• The logo attached must be included.
• The rear side of the card is dedicated to job quoted and price of the job.
• *Please include- Quote price, Quote date. etc
• Including the tasks I do at work around the side of the card- Gutter Cleaning; Roof Cleaning, Gutter Maintenance; Gardening; Pressure Cleaning Roof's, Driveways etc.
Nice to have
• The rear side to have a ladder

```html
<!DOCTYPE html>
<html lang="en">
<head>
<meta charset="utf-8">
<title>VERNO Business Card</title>
<link rel="stylesheet" href="https://fonts.googleapis.com/css2?family=Cinzel:wght@400&family=Arimo:wght@400;700&family=Roboto+Condensed:wght@400&display=swap">
<style>
  :root {
    --backdrop: #1b1b1d;
    --teal: #1fae9c;
    --teal-mid: #1f8fb0;
    --royal: #2c3a9f;
    --navy: #2b3594;
    --white: #ffffff;
    --ink-blue: #2b3594;
  }
  * { box-sizing: border-box; margin: 0; padding: 0; }
  html, body {
    width: 1200px;
    height: 1068px;
    overflow: hidden;
    background: var(--backdrop);
  }
  .sheet {
    position: relative;
    width: 1200px;
    height: 1068px;
  }
  .card {
    position: absolute;
    top: 380px;
    width: 560px;
    height: 308px;
    overflow: hidden;
    color: var(--white);
  }
  .card--front {
    left: 28px;
    background: linear-gradient(180deg, var(--teal) 0%, var(--teal) 38%, var(--teal-mid) 58%, var(--royal) 78%, var(--royal) 100%);
  }
  .card--back {
    left: 612px;
    background: var(--navy);
    font-family: "Arimo", Arial, sans-serif;
  }

  /* front */
  .brand-name {
    position: absolute;
    left: 40px;
    top: 74px;
    font-family: "Cinzel", "Times New Roman", serif;
    font-weight: 400;
    font-size: 112px;
    line-height: 1;
    letter-spacing: 1px;
    color: var(--white);
  }
  .brand-mark {
    position: absolute;
    left: 462px;
    top: 52px;
    width: 70px;
    height: 70px;
    border-radius: 50%;
    background: var(--white);
    opacity: 0.85;
  }
  .tagline {
    position: absolute;
    left: 22px;
    top: 184px;
    font-family: "Roboto Condensed", Arial, sans-serif;
    font-size: 14.5px;
    letter-spacing: 0.2px;
    text-transform: uppercase;
  }
  .director {
    position: absolute;
    left: 0;
    width: 100%;
    top: 238px;
    text-align: center;
    font-family: "Cinzel", "Times New Roman", serif;
    font-size: 27px;
    letter-spacing: 1px;
  }

  /* back */
  .contact {
    position: absolute;
    top: 16px;
    width: 100%;
    text-align: center;
    font-size: 17px;
    line-height: 24px;
  }
  .services {
    position: absolute;
    top: 98px;
    left: 26px;
    list-style: none;
    font-size: 17.5px;
    line-height: 23.5px;
  }
  .services li::before {
    content: "";
    display: inline-block;
    width: 0;
    height: 0;
    border-top: 5px solid transparent;
    border-bottom: 5px solid transparent;
    border-left: 9px solid var(--white);
    margin-right: 6px;
    vertical-align: 1px;
  }
  .credentials {
    position: absolute;
    top: 209px;
    width: 100%;
    text-align: center;
    font-size: 17px;
    line-height: 24px;
  }
  .quote-strip {
    position: absolute;
    left: 0;
    bottom: 0;
    width: 100%;
    height: 40px;
    background: var(--white);
    color: var(--ink-blue);
    font-weight: 700;
    font-size: 18px;
  }
  .quote-strip span {
    position: absolute;
    top: 10px;
  }
  .quote-label { left: 34px; }
  .date-label { left: 396px; }
</style>
</head>
<body>
<main class="sheet">
  <section class="card card--front" aria-label="Card front">
    <div class="brand-name">VERNO</div>
    <div class="brand-mark" aria-hidden="true"></div>
    <p class="tagline">Roof, Gutter &amp; Pressure Cleaning Services</p>
    <p class="director">Dale Marwick, Director</p>
  </section>

  <section class="card card--back" aria-label="Card back">
    <div class="contact">
      <p>0417385026</p>
      <p>roofcleaning@plovernet.example.au</p>
      <p>ABN -48 902 317 254</p>
    </div>
    <ul class="services">
      <li>Gutter Cleaning</li>
      <li>Pressure Cleaning: Roofs, Driveways etc.</li>
      <li>Minor Roof, Gutter &amp; Building Maintenance</li>
      <li>Garden Waste Removal &amp; Complex Cleanups</li>
    </ul>
    <div class="credentials">
      <p>Public Liability Up to $10 Million</p>
      <p>Working at Heights Cert.</p>
    </div>
    <div class="quote-strip">
      <span class="quote-label">Quote:</span>
      <span class="date-label">Date:</span>
    </div>
  </section>
</main>
</body>
</html>
```